INNOVATIVE DESIGN NEEDED FOR FINANCIAL COMPANY

INTERNATIONAL FIRM IN HONG KONG NEEDS A MODERN BUSINESS CARD DESIGN. ONE SIDE ENGLISH OTHER SIDE IN CHINESE. WE ARE OPEN TO CHANGING FONTS AND COLOR. SHOULD BE A CARD THAT IS PROFESSIONAL DEALING WITH HIGH NET WORTH CLIENTELE. BOTH SIDES OF THE CARD WILL BE THE SAME, HOWEVER, THE WORDING ON ONE SIDE WILL BE ENGLISH AND THE OTHER SIDE IN CHINESE (CAN ASSIST IN THE LETTERING - CAN PROVIDE ONCE CARD DESIGN IS ACCEPTED.

Target Market(s)

Hong Kong/CHINA

Contact Information for Business Card

ATTRACTIVE MODERN

```html
<!DOCTYPE html>
<html lang="en">
<head>
<meta charset="utf-8">
<title>Linden Crest Wealth Ltd – Business Card</title>
<link href="https://fonts.googleapis.com/css2?family=Roboto:ital,wght@0,400;0,500;0,700;1,400&family=Noto+Sans+SC:wght@500;700;900&display=swap" rel="stylesheet">
<style>
  :root{
    --green:#15906a;
    --ink:#4a4a4c;
    --paper:#ffffff;
    --stage:#e9e9ea;
  }
  *{box-sizing:border-box;margin:0;padding:0}
  html,body{width:1200px;height:1200px;overflow:hidden;background:var(--stage)}
  body{font-family:"Roboto",sans-serif;position:relative}
  .card{position:absolute;left:150px;width:900px;height:514px;border-radius:30px;overflow:hidden}
  .card--chinese{top:48px;background:var(--green);color:var(--paper)}
  .card--english{top:638px;background:var(--paper);color:var(--ink)}
  .card__band{position:absolute;left:0;right:0;bottom:0;height:46px;background:var(--green)}
  .brand{position:absolute;left:290px;top:72px;display:flex;align-items:center;gap:20px;white-space:nowrap}
  .brand__dot{width:90px;height:90px;border-radius:50%;flex:none}
  .card--chinese .brand__dot{background:var(--paper)}
  .card--english .brand__dot{background:var(--green)}
  .brand__name{font-family:"Noto Sans SC",sans-serif;font-weight:900;line-height:1.1;display:block}
  .brand__zh{font-size:42px;letter-spacing:1px;display:block}
  .brand__en{font-size:22px;letter-spacing:3.2px;display:block;margin-top:4px}
  .card--chinese .brand__name{color:var(--paper)}
  .card--english .brand__name{color:var(--ink)}
  .person{position:absolute;left:60px;top:210px}
  .person__name{font-size:38px;font-weight:700;line-height:1.1;white-space:nowrap}
  .card--chinese .person__name{font-family:"Noto Sans SC",sans-serif;font-size:40px}
  .card--english .person__name{color:var(--green);font-weight:500;font-size:36px}
  .person__role{font-size:24px;margin-top:4px}
  .card--chinese .person__role{font-family:"Noto Sans SC",sans-serif;font-weight:700}
  .contact{position:absolute;left:60px;top:320px;list-style:none;font-size:24px;line-height:40px}
  .contact li{display:flex;align-items:center;gap:14px;white-space:nowrap}
  .contact svg{width:22px;height:22px;flex:none}
  .card--chinese .contact svg{stroke:var(--paper)}
  .card--english .contact svg{stroke:var(--green)}
  .address{position:absolute;right:60px;bottom:90px;text-align:right;font-size:25px;line-height:34px;font-weight:500;white-space:nowrap}
  .card--chinese .address{bottom:60px}
</style>
</head>
<body>

<section class="card card--chinese" aria-label="Chinese side">
  <div class="brand">
    <span class="brand__dot"></span>
    <span class="brand__name"><span class="brand__zh">林峰財富管理有限公司</span><span class="brand__en">Linden Crest Wealth Ltd</span></span>
  </div>
  <div class="person">
    <p class="person__name">丹尼尔·卡特</p>
    <p class="person__role">总裁</p>
  </div>
  <ul class="contact">
    <li><svg viewBox="0 0 24 24" fill="none" stroke-width="2"><path d="M5 3h4l2 5-3 2a12 12 0 0 0 6 6l2-3 5 2v4a2 2 0 0 1-2 2A18 18 0 0 1 3 5a2 2 0 0 1 2-2z"/></svg>(852) 2310 - 4588</li>
    <li><svg viewBox="0 0 24 24" fill="none" stroke-width="2"><rect x="2" y="5" width="20" height="14" rx="1"/><path d="M2 6l10 7 10-7"/></svg>info@lindencrest.com</li>
    <li><svg viewBox="0 0 24 24" fill="none" stroke-width="2"><circle cx="12" cy="12" r="10"/><path d="M2 12h20M12 2c3 3 3 17 0 20M12 2c-3 3-3 17 0 20"/></svg>www.lindencrest.com</li>
  </ul>
  <p class="address">215, Maple Grove Avenue,<br>Suite C, Fairview, NY 10472</p>
</section>

<section class="card card--english" aria-label="English side">
  <div class="brand">
    <span class="brand__dot"></span>
    <span class="brand__name"><span class="brand__zh">林峰財富管理有限公司</span><span class="brand__en">Linden Crest Wealth Ltd</span></span>
  </div>
  <div class="person">
    <p class="person__name">DANIEL LEE CARTER</p>
    <p class="person__role">Chief Executive</p>
  </div>
  <ul class="contact">
    <li><svg viewBox="0 0 24 24" fill="none" stroke-width="2"><path d="M5 3h4l2 5-3 2a12 12 0 0 0 6 6l2-3 5 2v4a2 2 0 0 1-2 2A18 18 0 0 1 3 5a2 2 0 0 1 2-2z"/></svg>(852) 2310 - 4588</li>
    <li><svg viewBox="0 0 24 24" fill="none" stroke-width="2"><rect x="2" y="5" width="20" height="14" rx="1"/><path d="M2 6l10 7 10-7"/></svg>info@lindencrest.com</li>
    <li><svg viewBox="0 0 24 24" fill="none" stroke-width="2"><circle cx="12" cy="12" r="10"/><path d="M2 12h20M12 2c3 3 3 17 0 20M12 2c-3 3-3 17 0 20"/></svg>www.lindencrest.com</li>
  </ul>
  <p class="address">215, Maple Grove Avenue,<br>Suite C, Fairview, NY 10472</p>
  <div class="card__band"></div>
</section>

</body>
</html>
```